Boracay Wedding Invitation Design

Hello, We would like a wedding invitation design for our wedding in Boracay. We would like it somewhat in the form of a boarding pass with beachy fresh colours, possibly a nice Boracay beach in the background Double sided with an envelope design to match. Maybe something simple on the envelope like a nice picture in the bottom left corner of a shell on a beach or something similar.

I would also like on the opposite side of the invite to be an "information sheet" with a matching beach design

The text files for both sides are included and i have also included 2 designs that i thought looked nice and are similar to what we are after.
Updates

Hello, I have updated the brief to be more specific with text files and images to make it easier for you. Thank you :)

Industry/Entity Type

Wedding

Font styles to use
Decorative
Script

Colors
fbee3d
33a6d7
33b8a4
fbf289
85cae6
ffffff

Requirements
Must have
• I would like to have this quote somewhere on the invitation
• This day I will marry my best friend,
• the one I laugh with,
• live for,
• dream with,
• love
• Owen & Marisa
• Request the pleasure of your company to celebrate their wedding
• On Friday the 17th March 2017
• at
• Velunda Grand Suites
• Boracay, Philippines
• Ceremony begins at 3.00pm
• RSVP
• Owen 0431907254
• Marisa 0417283649
• by
• 17th Jan 2016
• Dress: Beach Formal
• For the "information sheet"
• There will be a 5% discount on rooms booked at the Velunda under the event Owen & Marisa Wedding. The resort has a total of 24 rooms it would be nice if the majority of guests could stay at the resort from the night before until the night after the wedding but if you choose to stay elsewhere on the island there are plenty of other places to stay for cheaper and everything is fairly close as its a small island.
• We have currently blocked room stay for a short period of time so our guests can book rooms. If you choose to do so please email reservations@velundastays.example. Once rooms become available to the public again, towards the end of Jan, it will be first come first served basis. The resort is very popular so im assuming once this happens the rooms will be booked out.
• If you would like to check out the resort itself the website is www.velundagrand-isle.example
• We know its a fair distance to travel but we would really love to see you all there to celebrate and maybe even enjoy a small holiday while your here its a beautiful part of the world.
• If anyone has any questions please feel free to contact Owen on 0431907254
Nice to have
• A nice picture of a Boracay beach in the background would be nice

```html
<!DOCTYPE html>
<html lang="en">
<head>
<meta charset="utf-8">
<title>Owen &amp; Marisa – Wedding Invitation</title>
<link rel="stylesheet" href="https://fonts.googleapis.com/css2?family=Italianno&family=Delius&family=Arimo&display=swap">
<style>
  :root {
    --frame: #000000;
    --label-band: #d4d4d6;
    --label-ink: #333333;
    --ink: #2b5ba8;
    --sky-light: #eaf7fd;
    --sky-mid: #9fd6ee;
    --sky-deep: #4fb2e0;
    --paper: #ffffff;
    --box: rgba(255,255,255,0.4);
  }
  * { margin: 0; padding: 0; box-sizing: border-box; }
  html, body { width: 1200px; height: 674px; overflow: hidden; background: var(--frame); }
  .canvas { position: relative; width: 1200px; height: 674px; background: var(--frame); }

  .panel { position: absolute; top: 29px; width: 570px; height: 570px; overflow: hidden; }
  .panel--back { left: 28px; }
  .panel--front { left: 600px; }

  .panel__pattern { position: absolute; inset: 0; }
  .panel--back .panel__pattern {
    background: radial-gradient(ellipse 62% 58% at 50% 42%, var(--sky-light) 0%, var(--sky-mid) 58%, var(--sky-deep) 100%);
  }
  .panel--front .panel__pattern {
    background:
      linear-gradient(180deg, var(--paper) 0%, var(--paper) 24%, rgba(255,255,255,0) 40%),
      radial-gradient(ellipse 65% 60% at 50% 62%, var(--sky-light) 0%, var(--sky-mid) 55%, var(--sky-deep) 100%);
  }

  .line { position: absolute; left: 0; width: 100%; text-align: center; color: var(--ink); white-space: nowrap; line-height: 1; }
  .quote { font-family: "Italianno", cursive; font-size: 34px; }
  .detail { font-family: "Delius", cursive; font-size: 24px; }

  .ceremony-box { position: absolute; left: 118px; top: 515px; width: 334px; height: 32px; background: var(--box); }

  .couple { position: absolute; margin: 0; font-family: "Italianno", cursive; font-weight: 400; color: var(--ink); line-height: 1; white-space: nowrap; }
  .couple--first { left: 2px; top: 52px; font-size: 135px; }
  .couple--amp { left: 232px; top: 40px; font-size: 120px; }
  .couple--second { left: 180px; top: 100px; font-size: 165px; }

  .labels { position: absolute; left: 0; top: 629px; width: 1200px; height: 45px; background: var(--label-band); }
  .labels__item { position: absolute; top: 11px; width: 300px; text-align: center; font-family: "Arimo", sans-serif; font-size: 22px; color: var(--label-ink); }
  .labels__item--back { left: 163px; }
  .labels__item--front { left: 734px; }
</style>
</head>
<body>
<main class="canvas">
  <section class="panel panel--back">
    <div class="panel__pattern" role="img" aria-label="Light blue swirling shell-like line pattern"></div>
    <p class="line quote" style="top:44px">This day I will marry</p>
    <p class="line quote" style="top:100px">my best friend,</p>
    <p class="line quote" style="top:155px">the one I laugh with,</p>
    <p class="line quote" style="top:205px">live for,</p>
    <p class="line quote" style="top:262px">dream with,</p>
    <p class="line quote" style="top:315px">love</p>
    <p class="line detail" style="top:360px">RSVP</p>
    <p class="line detail" style="top:390px">Owen – 0431907254</p>
    <p class="line detail" style="top:420px">Marisa – 0417283649</p>
    <p class="line detail" style="top:450px">by</p>
    <p class="line detail" style="top:479px">17th Jan 2016</p>
    <div class="ceremony-box"></div>
    <p class="line detail" style="top:520px">Ceremony begins at 3.00pm</p>
  </section>

  <section class="panel panel--front">
    <div class="panel__pattern" role="img" aria-label="Light blue swirling shell-like line pattern below a white band"></div>
    <h1 class="couple couple--first">Owen</h1>
    <span class="couple couple--amp">&amp;</span>
    <span class="couple couple--second">Marisa</span>
    <p class="line detail" style="top:340px">Request the pleasure of your company</p>
    <p class="line detail" style="top:369px">to celebrate their wedding</p>
    <p class="line detail" style="top:398px">On Friday,</p>
    <p class="line detail" style="top:427px">17th March 2017</p>
    <p class="line detail" style="top:456px">at</p>
    <p class="line detail" style="top:486px">Velunda Grand Suites</p>
    <p class="line detail" style="top:515px">Boracay, Philippines.</p>
  </section>

  <div class="labels">
    <span class="labels__item labels__item--back">BACK INSIDE</span>
    <span class="labels__item labels__item--front">FRONT INSIDE</span>
  </div>
</main>
</body>
</html>
```